Clara Joy Halden- Lantern Waltz- Autumn/Winter Tour Dates

I need high res A3 Tour poster for print and for social media JPG sharing of tour dates.
Also needed Facebook/Twitter Banner Cover Photos of these dates.
Text Needed Below
Clara Joy Halden
Lantern Waltz
Autumn/Winter Tour Dates
03/09 Ravensby Folk Festival
21/09 Swindon- Calder Theatre
01/10 Hitchin- Brackwell Folk Club
17/10 Bath- The Anvil
20/10 Sheffield- Upper Dale Croquet Club
24/10 Birmingham- Orchard Lamp Cafe
26/10 Glasgow- The Nook and Jar
27/10 Edinburgh - The Marble Parlour
08/11 Capital Reel and Ballad Festival- The Crooked Heron
25/11 Lewes- Tandem Record Shop- Live In Store
02/12 Cambridge- The Quayside
27/01 Lincolnshire- Fenmarsh Theatre
Tickets/Info: www.clarajoyhalden-music.example/gigs
(Quotes/Reviews To Put On)
"Outstanding, rich and expressive."            "Vibrant and Experimental"
**** BdM                                                               **** Tunepaths
"Impressive and Invigorating"                        "Enchanting" Acoustic Wire UK
tBarks

Updates
I cannot read the tour dates on most of the submissions so far. They need to be visible to viewers.
Thank You.
Please also be as creative and inventive as possible- not bland.

Target Market(s)
Music Fans- Folk Acoustic Americana
Industry/Entity Type
Media
Font styles to use
Requirements
Must have
- My photo featured prominently
- Look classy and not tacky or OTT
- Look elegant, wintery and eye catching
- The dates must be very clear to read
- Links to Website:

Nice to have
- Something innovative and not boring in terms of layout design
- Perhaps fading/ misty or wintery

Should not have
- Any colours that do not match

```html
<!DOCTYPE html>
<html lang="en">
<head>
<meta charset="utf-8">
<title>Clara Joy Halden – Lantern Waltz Tour Poster</title>
<link href="https://fonts.googleapis.com/css2?family=Great+Vibes&family=Playball&family=Lato:ital,wght@0,400;0,700;1,400&display=swap" rel="stylesheet">
<style>
  :root {
    --page-bg: #e9e8e6;
    --navy-deep: #0f1220;
    --navy: #1a2236;
    --white: #f4f4f6;
    --silver: #d9dadc;
    --ink: #121212;
    --cream: #ece3d6;
    --star: #8f6fd0;
  }
  * { box-sizing: border-box; margin: 0; padding: 0; }
  html, body { width: 1200px; height: 1200px; overflow: hidden; background: var(--page-bg); }
  .poster {
    position: absolute; left: 170px; top: 45px; width: 860px; height: 1110px;
    background:
      radial-gradient(ellipse 520px 300px at 88% 6%, rgba(80,100,125,.55), transparent 70%),
      linear-gradient(180deg, var(--navy) 0%, var(--navy-deep) 45%, var(--navy-deep) 100%);
    overflow: hidden; color: var(--white); font-family: "Lato", sans-serif;
  }
  .portrait {
    position: absolute; right: 0; top: 220px; width: 470px; height: 780px;
    background:
      radial-gradient(ellipse 120px 150px at 55% 40%, rgba(150,140,155,.55), transparent 75%),
      radial-gradient(ellipse 260px 380px at 55% 50%, rgba(55,60,85,.9), transparent 80%),
      radial-gradient(ellipse 300px 420px at 60% 40%, rgba(60,70,100,.6), transparent 85%);
    z-index: 0;
  }
  .artist-name {
    position: relative; z-index: 1; text-align: center; padding-top: 30px;
    font-family: "Great Vibes", cursive; font-size: 62px; font-weight: 400;
    letter-spacing: 2px; line-height: 1.2;
  }
  .title-band {
    position: relative; z-index: 1; margin-top: 10px; height: 66px;
    background: linear-gradient(90deg, rgba(255,255,255,0) 0%, rgba(190,192,196,.5) 14%, var(--silver) 40%, #f5f5f5 55%, var(--silver) 72%, rgba(190,192,196,.3) 90%, rgba(255,255,255,0) 100%);
    display: flex; align-items: center; justify-content: center;
  }
  .tour-title { font-family: "Playball", cursive; font-size: 46px; color: var(--ink); font-weight: 400; line-height: 1; }
  .tour-label {
    position: relative; z-index: 1; display: flex; align-items: center; gap: 12px;
    margin: 16px 70px 0 70px; font-family: "Great Vibes", cursive; font-size: 22px; line-height: 1.2;
  }
  .tour-label::before, .tour-label::after { content: ""; flex: 1; height: 1px; background: rgba(255,255,255,.5); }
  .dates { position: relative; z-index: 1; list-style: none; margin: 30px 0 0 80px; }
  .dates li { display: grid; grid-template-columns: 130px 1fr; align-items: baseline; margin-bottom: 6px; }
  .date { font-size: 28px; font-weight: 700; line-height: 1.2; }
  .date::before { content: "•"; font-size: 18px; margin-right: 8px; vertical-align: middle; }
  .venue { font-size: 20px; line-height: 1.35; }
  .reviews { position: absolute; z-index: 1; left: 110px; top: 840px; width: 440px; }
  .reviews h2 { font-family: "Playball", cursive; font-weight: 400; font-size: 26px; line-height: 1.2; margin-bottom: 6px; }
  .reviews p { font-size: 13px; font-style: italic; text-align: center; line-height: 1.6; }
  .reviews .source { font-style: normal; font-weight: 700; }
  .stars { color: var(--star); letter-spacing: 2px; font-style: normal; }
  .link-band {
    position: absolute; left: 0; right: 0; top: 1010px; height: 46px; z-index: 1;
    background: linear-gradient(90deg, var(--cream), #f6f1ea 60%, var(--cream));
    display: flex; align-items: center; justify-content: center;
    color: var(--ink); font-size: 18px; letter-spacing: 2px;
  }
  .foot-band { position: absolute; left: 0; right: 0; bottom: 0; height: 26px; background: var(--cream); }
</style>
</head>
<body>
  <main class="poster">
    <div class="portrait" role="img" aria-label="Portrait photo of the singer with dark hair and a pearl headpiece in a misty wintery setting"></div>
    <h1 class="artist-name">Clara Joy Halden</h1>
    <div class="title-band"><span class="tour-title">Lantern Waltz</span></div>
    <div class="tour-label">• Autumn/Winter Tour Dates •</div>
    <ul class="dates">
      <li><span class="date">03/09</span><span class="venue">Ravensby Folk Festival</span></li>
      <li><span class="date">21/09</span><span class="venue">Swindon- Calder Theatre</span></li>
      <li><span class="date">01/10</span><span class="venue">Hitchin- Brackwell Folk Club</span></li>
      <li><span class="date">17/10</span><span class="venue">Bath- The Anvil</span></li>
      <li><span class="date">20/10</span><span class="venue">Sheffield- Upper Dale Croquet Club</span></li>
      <li><span class="date">24/10</span><span class="venue">Birmingham- Orchard Lamp Cafe</span></li>
      <li><span class="date">26/10</span><span class="venue">Glasgow- The Nook and Jar</span></li>
      <li><span class="date">27/10</span><span class="venue">Edinburgh - The Marble Parlour</span></li>
      <li><span class="date">08/11</span><span class="venue">Capital Reel and Ballad Festival-<br>The Crooked Heron</span></li>
      <li><span class="date">25/11</span><span class="venue">Lewes- Tandem Record Shop-<br>Live In Store</span></li>
      <li><span class="date">02/12</span><span class="venue">Cambridge- The Quayside</span></li>
      <li><span class="date">27/01</span><span class="venue">Lincolnshire- Fenmarsh Theatre</span></li>
    </ul>
    <section class="reviews">
      <h2>Reviews</h2>
      <p>"Outstanding, rich and expressive." &nbsp;"Vibrant and Experimental"</p>
      <p><span class="stars">★★★★</span> <span class="source">BdM</span> &nbsp;<span class="stars">★★★★</span> <span class="source">Tunepaths</span></p>
      <p>"Impressive and Invigorating" &nbsp;"Enchanting" Acoustic Wire UK</p>
      <p class="source">tBarks</p>
    </section>
    <div class="link-band">www.clarajoyhalden-music.example/gigs</div>
    <div class="foot-band"></div>
  </main>
</body>
</html>
```